依頼詳細
コーポレートカラーがオレンジなので、オレンジをベースにデザインをお願いしたいと思っております。
見やすさ、内容の伝わりやすさ、先進的なイメージを与えつつ、信頼できる雰囲気のチラシデザインだと嬉しいです。
イメージ画像や写真などは独自にご提案いただいて構いません。
よろしくお願い致します。
記載項目
素案のファイルを添付します
サイズ
A4
ページ数
両面
希望イメージ
シンプル 複雑
単色 カラフル
暗い 明るい
日常 高級
遊び心 厳粛
未来的 伝統的
女性的 男性的
希望する色
黄・オレンジ系
納品ファイル
• 高解像度JPG (.jpg)
• イラストレーター形式 (.ai)
• フォトショップ形式 (.psd)
• PNG形式 (.png)
補足説明

伝わりやすいデザインで、独自のキャッチコピー提案がありました。裏面も見やすい形でデザインしていただけてとてもよかったです。ありがとうございました。

この度はお忙しい中、ご提案いただきましてありがとうございました。
また機会がございましたら、ご提案いただけますと幸いです。

```html
<!DOCTYPE html>
<html lang="ja">
<head>
<meta charset="utf-8">
<title>AI業務自動化ソリューション</title>
<link href="https://fonts.googleapis.com/css2?family=Noto+Sans+JP:wght@400;500;700&display=swap" rel="stylesheet">
<style>
  :root {
    --orange: #f39800;
    --orange-deep: #ec7a00;
    --yellow: #ffd45a;
    --ink: #333333;
    --ink-soft: #4a4a4a;
    --paper: #ffffff;
  }
  * { box-sizing: border-box; margin: 0; padding: 0; }
  html, body { width: 848px; height: 1200px; overflow: hidden; background: var(--paper); }
  body { font-family: "Noto Sans JP", sans-serif; color: var(--ink); position: relative; }

  .hero-waves {
    position: absolute; left: 0; top: 0; width: 848px; height: 520px;
    background:
      radial-gradient(ellipse 620px 260px at 760px 40px, rgba(243,152,0,.85), rgba(255,212,90,.45) 55%, rgba(255,255,255,0) 80%),
      radial-gradient(ellipse 700px 200px at 200px 470px, rgba(255,200,60,.55), rgba(255,255,255,0) 75%),
      linear-gradient(160deg, #fff8e6 0%, #ffffff 45%, #fff2d6 100%);
  }
  .hero-title {
    position: absolute; left: 80px; top: 200px;
    font-size: 56px; font-weight: 500; line-height: 1.3; letter-spacing: 6px; color: var(--ink);
  }
  .hero-lead {
    position: absolute; left: 80px; top: 432px; width: 700px;
    font-size: 16px; line-height: 1.6; color: var(--ink-soft); font-weight: 500;
  }

  .section-head {
    position: absolute; left: 80px; top: 580px; width: 688px;
    display: flex; align-items: baseline; gap: 14px;
    padding-bottom: 10px; border-bottom: 2px solid var(--orange);
  }
  .section-num { font-size: 38px; color: var(--orange); font-weight: 500; }
  .section-name { font-size: 34px; font-weight: 500; letter-spacing: 2px; }

  .section-sub {
    position: absolute; left: 80px; top: 676px;
    font-size: 23px; font-weight: 500; letter-spacing: 1px;
  }
  .section-body {
    position: absolute; left: 80px; top: 730px; width: 690px;
    font-size: 15px; line-height: 1.75; color: var(--ink-soft);
  }

  .features { position: absolute; left: 80px; top: 845px; width: 688px; }
  .feature { display: flex; height: 100px; margin-bottom: 14px; }
  .feature-label {
    width: 230px; background: linear-gradient(90deg, var(--orange-deep), var(--orange));
    color: #fff; display: flex; align-items: center; gap: 14px; padding-left: 22px;
    font-size: 18px; font-weight: 500;
  }
  .feature-label svg { width: 30px; height: 30px; flex: none; }
  .feature-text {
    flex: 1; border: 2px solid var(--orange); border-left: none;
    display: flex; align-items: center; padding: 0 22px;
    font-size: 16px; line-height: 1.6; font-weight: 500;
  }
</style>
</head>
<body>
  <div class="hero-waves" role="img" aria-label="オレンジと黄色の流れるような抽象的な波のグラフィック"></div>

  <h1 class="hero-title">AI業務自動化<br>ソリューション</h1>
  <p class="hero-lead">AIによって業務を効率化・自動化し、お客様のパフォーマンス最大化を支援。<br>最適なデバイスの選定、ソフト・ハードの設置、テスト、PDCAサイクルまで<br>トータルに導入をサポート。</p>

  <div class="section-head">
    <span class="section-num">01</span>
    <span class="section-name">AI - 動画解析</span>
  </div>
  <p class="section-sub">ヒト・モノ・コトの特徴をリアルタイムに検出</p>
  <p class="section-body">人物の所属情報の取得、製造・物流現場での不良品の検出、危険エリアへの侵入を検知。<br>人の目に頼っていた作業の自動化や、業務効率化、安全対策の支援を可能にします。</p>

  <div class="features">
    <div class="feature">
      <div class="feature-label">
        <svg viewBox="0 0 30 30" fill="none" stroke="#fff" stroke-width="2.4" stroke-linecap="round" stroke-linejoin="round"><path d="M3 16l6-5 5 3 6-5 7 6"/><path d="M9 18l5 4 4-3"/></svg>
        業務効率化支援
      </div>
      <div class="feature-text">お客様の業務の現状をしっかりと把握し、最適な改善案をご提案。プロセス全体での改善を図ります。</div>
    </div>
    <div class="feature">
      <div class="feature-label">
        <svg viewBox="0 0 30 30" fill="#fff"><path d="M15 3l3.5 7.5 8 1-6 5.6 1.6 8L15 21l-7.1 4.1 1.6-8-6-5.6 8-1z"/></svg>
        高精度の認識率
      </div>
      <div class="feature-text">AI画像認識ノウハウと効果的な学習を組み合わせることにより高精度の認識を実現させます。</div>
    </div>
    <div class="feature">
      <div class="feature-label">
        <svg viewBox="0 0 30 30" fill="#fff"><rect x="3" y="17" width="5" height="10"/><rect x="12" y="11" width="5" height="16"/><rect x="21" y="5" width="5" height="22"/></svg>
        解析＋アルファ
      </div>
      <div class="feature-text">解析するだけでなく、データの可視化・分析、デバイスへの通知等、柔軟に対応致します。</div>
    </div>
  </div>
</body>
</html>
```